An international wholesale business needs letterhead design

Logo file is attached. Please design a letterhead with the following details:

- Company Name and Logo
- Address
- VAT Registration number
- Phone No
- Website address

```html
<!DOCTYPE html>
<html lang="en">
<head>
<meta charset="utf-8">
<title>Corvane Trading Letterhead</title>
<link href="https://fonts.googleapis.com/css2?family=Montserrat:wght@300;400;500;600;700&display=swap" rel="stylesheet">
<style>
  :root {
    --brand-red: #c1272d;
    --ink-dark: #3a4750;
    --ink-body: #5a5f63;
    --rule-grey: #a9a9a9;
    --sheet-border: #8c8c8c;
    --paper: #ffffff;
    --footer-text: #ffffff;
  }
  * { margin: 0; padding: 0; box-sizing: border-box; }
  html, body {
    width: 1200px; height: 1000px; overflow: hidden;
    background: var(--paper);
    font-family: "Montserrat", Arial, sans-serif;
  }
  .canvas { position: relative; width: 1200px; height: 1000px; }
  .sheet {
    position: absolute; left: 243px; top: 0; width: 715px; height: 1000px;
    border-left: 1px solid var(--sheet-border);
    border-right: 1px solid var(--sheet-border);
    background: var(--paper);
  }
  .header-rule {
    position: absolute; left: 653px; top: 131px; width: 304px; height: 5px;
    background: var(--rule-grey);
  }
  .brand-name {
    position: absolute; left: 322px; top: 119px;
    color: var(--brand-red); font-weight: 600; font-size: 20px;
    letter-spacing: 0.3px; white-space: nowrap;
  }
  .letter-date {
    position: absolute; right: 326px; top: 185px;
    font-weight: 700; font-size: 14.5px; color: var(--ink-dark);
  }
  .salutation {
    position: absolute; left: 325px; top: 223px;
    font-weight: 600; font-size: 20px; color: var(--ink-dark);
  }
  .letter-body {
    position: absolute; left: 328px; top: 276px; width: 552px;
    font-size: 13.6px; font-weight: 400; line-height: 23.4px; color: var(--ink-body);
  }
  .letter-body p + p { margin-top: 31.4px; }
  .signature-area {
    position: absolute; left: 328px; top: 678px; width: 148px; height: 70px;
    background: linear-gradient(90deg, rgba(193,39,45,0.10), rgba(193,39,45,0.04));
    border-radius: 6px;
  }
  .signatory-name {
    position: absolute; left: 328px; top: 759px;
    font-weight: 700; font-size: 22px; color: var(--ink-dark);
  }
  .signatory-role {
    position: absolute; left: 328px; top: 792px;
    font-size: 17px; color: var(--ink-body);
  }
  .footer-band {
    position: absolute; left: 243px; top: 873px; width: 715px; height: 63px;
    background: var(--brand-red);
  }
  .footer-rule-thick {
    position: absolute; left: 243px; top: 940px; width: 715px; height: 10px;
    background: var(--rule-grey);
  }
  .footer-rule-thin {
    position: absolute; left: 243px; top: 954px; width: 715px; height: 4px;
    background: var(--rule-grey);
  }
  .contact-item {
    position: absolute; display: flex; align-items: center; gap: 9px;
    color: var(--footer-text); font-size: 9px; font-weight: 500;
    letter-spacing: 1px; text-transform: uppercase;
  }
  .contact-item svg { width: 13px; height: 13px; flex: none; }
  .contact-phone { left: 322px; top: 880px; }
  .contact-vat { left: 322px; top: 916px; }
  .contact-email { left: 738px; top: 879px; }
  .contact-web { left: 738px; top: 915px; }
</style>
</head>
<body>
<div class="canvas">
  <div class="sheet"></div>
  <div class="header-rule"></div>

  <div class="brand-name">CORVANE TRADING</div>

  <div class="letter-date">Date August 28, 2023</div>
  <div class="salutation">Dear Lukas Arden</div>

  <div class="letter-body">
    <p>Lorem ipsum dolor sit amet, consectetuer adipiscing elit, sed diam nonummy nibh euismod tincidunt ut laoreet dolore magna aliquam erat volutpat. Ut wisi enim ad minim veniam, quis nostrud exerci tation ullamcorper suscipit lobortis nisl ut aliquip ex ea commodo consequat.</p>
    <p>Duis autem vel eum iriure dolor in hendrerit in vulputate velit esse molestie con&shy;sequat, vel illum dolore eu feugiat nulla facilisis at vero eros et accumsan et iusto odio dignissim qui blandit praesent luptatum zzril delenit augue duis dolore te feugait nulla facilisi.</p>
    <p>Lorem ipsum dolor sit amet, consectetuer adipiscing elit, sed diam nonummy nibh euismod tincidunt ut laoreet dolore magna aliquam erat volutpat. Ut wisi enim ad minim veniam, quis nostrud exerci tation ullamcorper suscipit lobortis nisl ut aliquip ex ea commodo consequat.</p>
  </div>

  <div class="signature-area" role="img" aria-label="Handwritten signature of the general manager"></div>
  <div class="signatory-name">NAME SURNAME</div>
  <div class="signatory-role">General Manager</div>

  <div class="footer-band"></div>
  <div class="footer-rule-thick"></div>
  <div class="footer-rule-thin"></div>

  <div class="contact-item contact-phone">
    <svg viewBox="0 0 24 24" fill="none" stroke="#fff" stroke-width="2" stroke-linejoin="round"><path d="M5 3h4l2 5-3 2a12 12 0 0 0 6 6l2-3 5 2v4a2 2 0 0 1-2 2A17 17 0 0 1 3 5a2 2 0 0 1 2-2z"/></svg>
    <span>+99 999 999999</span>
  </div>
  <div class="contact-item contact-vat">
    <svg viewBox="0 0 24 24" fill="#fff"><path d="M5 2h10l4 4v16H5z"/><rect x="8" y="10" width="8" height="1.6" fill="#c1272d"/><rect x="8" y="14" width="8" height="1.6" fill="#c1272d"/><rect x="8" y="18" width="5" height="1.6" fill="#c1272d"/></svg>
    <span>AU12345678901</span>
  </div>
  <div class="contact-item contact-email">
    <svg viewBox="0 0 24 24" fill="none" stroke="#fff" stroke-width="2"><rect x="2" y="5" width="20" height="14"/><path d="M2 5l10 8 10-8"/></svg>
    <span>contact@corvane.com</span>
  </div>
  <div class="contact-item contact-web">
    <svg viewBox="0 0 24 24" fill="none" stroke="#fff" stroke-width="2"><circle cx="12" cy="12" r="10"/><path d="M2 12h20M12 2c3 3 3 17 0 20M12 2c-3 3-3 17 0 20"/></svg>
    <span>corvanetrading.com</span>
  </div>
</div>
</body>
</html>
```